Keelbrook Vault Holdings Needs A Website

We are looking for a website for a new company. 4 Pages

Needs to be responsive and mobile friendly for all browsers and coded for both Android & IOS. SEO is also important.

Website Brief – Keelbrook Vault Holdings
Domain: www.keelbrookvault.net
Email: info@keelbrookvault.net
Phone: to be inserted later
Address: 40837 52 Ave, Edmonton, AB T6K 3R8
Platform: WordPress (recommended for flexibility, SEO tools, and ease of editing)
Requirements:
• Responsive & mobile-friendly (Android & iOS)
• Cross-browser compatibility
• Fast page load speed
• SEO optimized for storage development, management, and investment keywords
• Easy in-house editing after launch
• Professional, modern, trust-driven design reflecting expertise, reliability, and innovation
________________________________________
Pages
1. HOME
Purpose: Quickly communicate who Keelbrook Vault Holdings is and why they’re the best choice for designing, building, leasing, and managing self storage facilities.
Content Highlights:
• Hero Section: Large, bold image of a modern self storage facility with headline:
"From Concept to Capacity – Your Self Storage Experts"
• Subheadline: “Keelbrook Vault Holdings delivers turnkey design, construction, leasing, and management services for profitable self storage operations.”
• Quick Service Icons:
o Facility Design & Development
o Construction & Build Management
o Lease-Up & Marketing
o Ongoing Facility Management
• Call to Action Button: “LEARN MORE” → links to ABOUT US page.
• Featured Project Highlights: Showcase a few completed or current projects with photos and stats.
• Contact Banner: “Ready to build your next self storage project? Let’s talk.” → CONTACT page.
2. ABOUT US
Purpose: Build credibility, showcase experience, and explain the value proposition.
Content Highlights:
• Who We Are: Overview of Keelbrook Vault Holdings’ history, mission, and team expertise.
• Our Approach: End-to-end process from site selection to occupancy.
• Why Choose Us:
o Industry expertise in self storage
o Proven track record in lease-up success
o Strong vendor and contractor network
3. SERVICES
Purpose: Detail all service offerings with clarity and authority.
Sections:
• Design & Development: Market analysis, site planning, and architectural design.
• Construction Management: Overseeing timelines, budgets, and quality control.
• Lease-Up Strategy: Marketing, promotions, and occupancy acceleration.
• Ongoing Facility Management: Staffing, maintenance, revenue optimization.

4. CONTACT
Purpose: Provide simple, direct ways to connect.
Content Highlights:
• Contact Form (Name, Email, Phone, Message)
• Direct Email: info@keelbrookvault.net
• Phone (if applicable)
• Google Map embed (if there’s a head office location)
• CTA: “Let’s Build Your Storage Success Story.”
Design & Technical Notes
• Visual Style: Clean, modern, bold typography, professional color palette (to be based on branding), strong imagery of self storage facilities.
• Performance: Image compression, caching, responsive scaling.
• SEO Targets: “Self storage facility developer,” “self storage construction,” “self storage management company,” “lease-up services for self storage.”

WordPress or Joomla – must be desktop and mobile friendly with fast page load speed. Need the ability to edit ourselves.

Use pantone colours - #033c5a – dark blue
#2baadf – light blue

```html
<!DOCTYPE html>
<html lang="en">
<head>
<meta charset="utf-8">
<title>Keelbrook Vault Holdings – Self Storage Experts</title>
<link href="https://fonts.googleapis.com/css2?family=Poppins:wght@400;500;600;700;800&display=swap" rel="stylesheet">
<style>
:root{
  --dark:#033c5a;
  --light:#2baadf;
  --ink:#1c2430;
  --pale:#f4f6fa;
  --white:#ffffff;
}
*{box-sizing:border-box;margin:0;padding:0}
html,body{width:1200px;height:3319px;overflow:hidden}
body{font-family:'Poppins',sans-serif;color:var(--ink);background:var(--white);position:relative}
.topbar{height:44px;background:var(--light);position:relative;color:var(--white);font-size:15px;font-weight:600}
.topbar-left{position:absolute;left:0;top:0;height:44px;width:470px;background:var(--dark);clip-path:polygon(0 0,100% 0,calc(100% - 18px) 100%,0 100%)}
.topbar span{position:absolute;top:12px;display:flex;align-items:center;gap:6px}
.topbar svg{width:14px;height:14px;fill:var(--white)}
.nav{height:93px;display:flex;align-items:center;justify-content:space-between;padding:0 127px 0 115px}
.brand{display:flex;align-items:center;gap:10px;font-weight:700;font-size:22px;color:var(--dark)}
.brand-mark{width:30px;height:30px;background:var(--dark)}
.nav ul{list-style:none;display:flex;gap:47px;font-size:15px;font-weight:600;color:var(--dark)}
.nav li.active{color:var(--light)}
.hero{position:relative;height:604px;background:linear-gradient(180deg,#c9d9e8 0%,#e6eef5 40%,#b8c8d6 72%,#8c96a0 100%);text-align:center}
.hero-photo{position:absolute;inset:0}
.hero h1{position:relative;padding-top:50px;font-size:36px;font-weight:800;line-height:43px;color:var(--dark);text-transform:uppercase}
.hero p{position:relative;margin:12px auto 0;width:500px;font-size:18px;line-height:22px;color:var(--ink)}
.hero-edge{position:absolute;left:0;bottom:0;width:1200px;height:112px}
.services{background:var(--pale);height:451px;text-align:center;padding-top:10px}
.section-title{font-size:33px;font-weight:800;color:var(--dark);text-transform:uppercase;line-height:40px}
.section-title em{font-style:normal;color:var(--light)}
.rule{width:72px;height:3px;background:var(--light);margin:12px auto 0}
.service-row{display:flex;justify-content:center;margin-top:38px;margin-left:128px;width:944px}
.service{flex:1;display:flex;flex-direction:column;align-items:center;border-right:1px solid #cfd6de;height:168px}
.service:last-child{border-right:none}
.service-icon{width:104px;height:104px;border-radius:50%;background:var(--light);display:flex;align-items:center;justify-content:center}
.service-icon svg{width:54px;height:54px;fill:none;stroke:var(--white);stroke-width:2.2;stroke-linecap:round;stroke-linejoin:round}
.service h3{margin-top:20px;font-size:17px;font-weight:600;line-height:22px;color:var(--ink)}
.btn{display:inline-block;border-radius:24px;font-weight:600;text-transform:uppercase;color:var(--white)}
.btn-dark{background:var(--dark);font-size:16px;padding:13px 29px;margin-top:43px}
.projects{text-align:center;padding-top:118px;height:1208px}
.grid{width:944px;margin:34px auto 0;display:grid;gap:13px}
.grid-row{display:grid;gap:13px}
.row-3{grid-template-columns:repeat(3,1fr);height:272px}
.row-2{grid-template-columns:468px 1fr;height:294px}
.photo{border-radius:4px}
.p-sky{background:linear-gradient(180deg,#a9c6e2 0%,#e4ebf1 55%,#8d939a 100%)}
.p-ware{background:linear-gradient(180deg,#6d7a8a 0%,#b58a5e 50%,#9aa5ae 100%)}
.p-blue{background:linear-gradient(180deg,#2f7fd0 0%,#cfd7dd 55%,#b3b7bb 100%)}
.p-yellow{background:linear-gradient(180deg,#7eb3e6 0%,#c3cad1 55%,#c9b348 80%,#c7c3bc 100%)}
.cta{position:relative;height:510px;background:linear-gradient(180deg,#0d3a5f 0%,#174a72 50%,#0e3f66 100%);text-align:center;color:var(--white)}
.cta h2{position:relative;padding-top:172px;font-size:35px;font-weight:700;line-height:41px;text-transform:uppercase}
.btn-light{position:relative;background:var(--light);font-size:18px;padding:9px 25px;margin-top:32px;text-transform:uppercase}
.cta-edge{position:absolute;left:0;bottom:0;width:1200px;height:110px}
.footer{position:relative;height:409px}
.footer-about{position:absolute;left:127px;top:80px;width:370px}
.footer-about .brand{font-size:22px}
.footer-about p{margin-top:30px;font-size:15px;line-height:23px;color:#2b3a55}
.socials{display:flex;gap:8px;margin-top:18px}
.socials span{width:38px;height:38px;border-radius:50%;border:1.5px solid var(--light)}
.footer h4{font-size:21px;font-weight:700;color:var(--dark);text-transform:uppercase}
.footer-contact{position:absolute;left:571px;top:96px}
.contact-item{display:flex;align-items:center;gap:14px;margin-top:16px;font-size:15px;line-height:18px;color:#2b3a55}
.contact-item:first-of-type{margin-top:18px}
.contact-icon{width:37px;height:37px;border-radius:6px;background:var(--light);display:flex;align-items:center;justify-content:center;flex-shrink:0}
.contact-icon svg{width:22px;height:22px;fill:none;stroke:var(--white);stroke-width:1.8}
.footer-links{position:absolute;left:932px;top:96px}
.footer-links ul{list-style:none;margin-top:16px;font-size:15px;color:#2b3a55}
.footer-links li{margin-bottom:11px}
.copyright{position:absolute;left:0;right:0;top:370px;text-align:center;font-size:14px;color:#2b3a55}
</style>
</head>
<body>
<header>
  <div class="topbar">
    <div class="topbar-left"></div>
    <span style="left:127px"><svg viewBox="0 0 16 16"><path d="M1 3h14v10H1z M1 3l7 6 7-6" fill="none" stroke="#fff" stroke-width="1.6"/></svg>info@keelbrookvault.net</span>
    <span style="left:550px"><svg viewBox="0 0 16 16"><path d="M8 1a5 5 0 0 0-5 5c0 4 5 9 5 9s5-5 5-9a5 5 0 0 0-5-5zm0 7a2 2 0 1 1 0-4 2 2 0 0 1 0 4z"/></svg>40837 52 Ave, Edmonton, AB T6K 3R8</span>
    <span style="left:903px"><svg viewBox="0 0 16 16"><path d="M3 1l3 3-2 2c1 2 3 4 5 5l2-2 3 3-2 3C7 14 2 9 1 3z"/></svg>Call: 0004 555 0187</span>
  </div>
  <nav class="nav">
    <div class="brand"><span class="brand-mark"></span>Keelbrook Vault Holdings</div>
    <ul>
      <li class="active">HOME</li>
      <li>ABOUT US</li>
      <li>SERVICES</li>
      <li>CONTACT</li>
    </ul>
  </nav>
</header>

<section class="hero">
  <div class="hero-photo" role="img" aria-label="Modern white and blue self storage facility with a large roll-up door under a cloudy sky"></div>
  <h1>From Concept to Capacity<br>Your Self Storage Experts</h1>
  <p>Keelbrook Vault Holdings delivers turnkey design, construction, leasing, and management services for profitable self storage operations.</p>
  <svg class="hero-edge" viewBox="0 0 1200 112" preserveAspectRatio="none">
    <polygon points="0,112 600,0 1200,112" fill="#033c5a"/>
    <polygon points="0,112 600,40 1200,112" fill="#f4f6fa"/>
    <polygon points="600,0 1150,95 1200,92 1200,112 1180,112" fill="#f4f6fa"/>
  </svg>
</section>

<section class="services">
  <h2 class="section-title">Quick <em>Services</em></h2>
  <div class="rule"></div>
  <div class="service-row">
    <div class="service">
      <div class="service-icon"><svg viewBox="0 0 48 48"><rect x="8" y="8" width="26" height="32" rx="2"/><path d="M13 16h16M13 22h10"/><circle cx="34" cy="32" r="7"/><circle cx="34" cy="32" r="2.5"/></svg></div>
      <h3>Facility Design &amp;<br>Development</h3>
    </div>
    <div class="service">
      <div class="service-icon"><svg viewBox="0 0 48 48"><path d="M12 22a12 12 0 0 1 24 0"/><path d="M9 22h30"/><path d="M24 10v6"/><path d="M10 42c2-7 7-10 14-10s12 3 14 10"/></svg></div>
      <h3>Construction &amp;<br>Build Management</h3>
    </div>
    <div class="service">
      <div class="service-icon"><svg viewBox="0 0 48 48"><rect x="6" y="10" width="14" height="12" rx="2"/><rect x="28" y="8" width="12" height="10" rx="2"/><rect x="30" y="26" width="10" height="10" rx="2"/><path d="M10 40l10-10 6 4 4-6"/></svg></div>
      <h3>Lease-Up<br>&amp; Marketing</h3>
    </div>
    <div class="service">
      <div class="service-icon"><svg viewBox="0 0 48 48"><circle cx="24" cy="16" r="7"/><circle cx="24" cy="16" r="2.5"/><path d="M10 40v-6a5 5 0 0 1 10 0v6M28 40v-6a5 5 0 0 1 10 0v6M19 40v-4a5 5 0 0 1 10 0v4"/></svg></div>
      <h3>Ongoing Facility<br>Management</h3>
    </div>
  </div>
  <a class="btn btn-dark">Learn More</a>
</section>

<section class="projects">
  <h2 class="section-title">Current <em>Projects</em></h2>
  <div class="rule"></div>
  <div class="grid">
    <div class="grid-row row-3">
      <div class="photo p-sky" role="img" aria-label="White storage building with blue trim and roll-up door"></div>
      <div class="photo p-ware" role="img" aria-label="Warehouse shelving stacked with boxes beside a delivery van"></div>
      <div class="photo p-ware" role="img" aria-label="Warehouse aisle with pallet racks and a forklift"></div>
    </div>
    <div class="grid-row row-2">
      <div class="photo p-blue" role="img" aria-label="Long corrugated metal warehouse under a blue sky"></div>
      <div class="photo p-yellow" role="img" aria-label="Row of storage units with yellow doors"></div>
    </div>
    <div class="grid-row row-3">
      <div class="photo p-ware" role="img" aria-label="Warehouse racks with pallets and a forklift"></div>
      <div class="photo p-blue" role="img" aria-label="Self storage units with blue roll-up doors"></div>
      <div class="photo p-blue" role="img" aria-label="White concrete storage building with a blue door"></div>
    </div>
  </div>
</section>

<section class="cta" role="img" aria-label="Dark blue tinted warehouse interior with shelves of boxes">
  <h2>Ready to build your next<br>self storage project?</h2>
  <a class="btn btn-light">Let’s Talk</a>
  <svg class="cta-edge" viewBox="0 0 1200 110" preserveAspectRatio="none">
    <polygon points="0,110 600,0 1200,110" fill="#2baadf"/>
    <polygon points="0,110 600,18 1200,110" fill="#ffffff"/>
    <polygon points="1100,92 1200,80 1200,110" fill="#ffffff"/>
  </svg>
</section>

<footer class="footer">
  <div class="footer-about">
    <div class="brand"><span class="brand-mark"></span>Keelbrook Vault Holdings</div>
    <p>Lorem ipsum dolor sit amet, consectetur adipiscing elit, sed do eiusmod tempor incididunt ut labore et dolore magna aliqua. Quis ipsum suspendisse ultrices gravida.</p>
    <div class="socials"><span></span><span></span></div>
  </div>
  <div class="footer-contact">
    <h4>Contact</h4>
    <div class="contact-item"><span class="contact-icon"><svg viewBox="0 0 24 24"><path d="M12 3a6 6 0 0 0-6 6c0 5 6 12 6 12s6-7 6-12a6 6 0 0 0-6-6z"/><circle cx="12" cy="9" r="2"/></svg></span><span>Address: 40837 52 Ave,<br>Edmonton, AB T6K 3R8</span></div>
    <div class="contact-item"><span class="contact-icon"><svg viewBox="0 0 24 24"><path d="M5 3l4 4-2 2c1 3 4 6 7 7l2-2 4 4-2 3C10 21 3 14 3 5z"/></svg></span><span>Phone:<br>780 555 0142</span></div>
    <div class="contact-item"><span class="contact-icon"><svg viewBox="0 0 24 24"><rect x="3" y="5" width="18" height="14" rx="1"/><path d="M3 6l9 7 9-7"/></svg></span><span>Email:<br>info@keelbrookvault.net</span></div>
  </div>
  <div class="footer-links">
    <h4>Links</h4>
    <ul><li>Home</li><li>About Us</li><li>Services</li><li>Contact</li></ul>
  </div>
  <p class="copyright">© 2025 Copyright - Keelbrook Vault Holdings.&nbsp; All Rights are Reserved.</p>
</footer>
</body>
</html>
```